E-commerce website needs a splash page ad

Our website, widgetburrow.com, needs an additional ad on our 'splash page'. It needs to fit within these dimensions: 980x383 pixels.

Please visit widgetburrow.com to see the slide in action, and to see what content already exists.

The splash ad needs to contain an image of the Norvale product we are selling, as well as the Norvale logo featured in one of the corners of the ad. A button need to be made (visual only) with the text "view page" or something akin to "take me to part of the website that sells this product"

The ad needs to be clean, modern, and aimed towards a mature audience- no flowery graphics are needed.

Target Market(s)

Families, senior citizens, homeowners, small business owners

Industry/Entity Type

Product

Font styles to use
Sans Serif

Colors

Designer to choose colors to be used in the design.

Requirements
Must have
• -Black background with large, white font that says (in one way or another) " outdoor motion detection lighting"
-Norvale logo must be present in one of the 4 corners
-must fit the 980x383 pixels size
-A light gray-to-white gradient somewhere in the background
- At least 2 Norvale images must be used (a white and black norvale, for example)
Nice to have
• -A cone-shaped white gradient emitting from one of the Norvale spotlights
- This white gradient will 'illuminate' a "view page" button (or 'buy now', etc)

```html
<!DOCTYPE html>
<html lang="en">
<head>
<meta charset="utf-8">
<title>Norvale – Outdoor Motion Detection Lighting</title>
<link rel="stylesheet" href="https://fonts.googleapis.com/css2?family=Oswald:wght@500;600&family=Open+Sans:wght@400;700&display=swap">
<style>
  :root {
    --bg-deep: #0b0b0b;
    --bg-glow: #3a3a3a;
    --headline: #ffffff;
    --brand-green: #8cc63f;
    --brand-green-dark: #5f9a1f;
    --tagline: #8cc63f;
    --button-text: #ffffff;
    --product-light: #e9ecef;
    --product-dark: #1c1d20;
  }
  * { margin: 0; padding: 0; box-sizing: border-box; }
  html, body {
    width: 1200px;
    height: 469px;
    overflow: hidden;
    background: var(--bg-deep);
  }
  .splash-ad {
    position: relative;
    width: 1200px;
    height: 469px;
    overflow: hidden;
    background:
      radial-gradient(ellipse 620px 420px at 520px 210px, var(--bg-glow) 0%, #1e1e1e 45%, var(--bg-deep) 100%);
  }
  .light-cone {
    position: absolute;
    inset: 0;
    width: 1200px;
    height: 469px;
  }
  .headline {
    position: absolute;
    left: 40px;
    top: 36px;
    width: 650px;
    text-align: center;
    font-family: "Oswald", "Arial Narrow", sans-serif;
    font-weight: 600;
    font-size: 76px;
    line-height: 79px;
    letter-spacing: 1px;
    color: var(--headline);
    text-transform: uppercase;
    text-shadow: 0 2px 6px rgba(0,0,0,0.6);
  }
  .brand {
    position: absolute;
    left: 142px;
    top: 360px;
    width: 340px;
  }
  .brand-name {
    display: flex;
    align-items: center;
    gap: 12px;
    font-family: "Open Sans", Arial, sans-serif;
    font-weight: 700;
    font-size: 40px;
    line-height: 44px;
    color: var(--brand-green);
  }
  .brand-mark {
    width: 18px;
    height: 18px;
    border-radius: 50%;
    background: var(--brand-green);
  }
  .brand-tagline {
    margin-top: 6px;
    font-family: "Open Sans", Arial, sans-serif;
    font-weight: 400;
    font-size: 19px;
    color: var(--tagline);
    white-space: nowrap;
  }
  .cta-button {
    position: absolute;
    left: 542px;
    top: 370px;
    width: 253px;
    height: 54px;
    border-radius: 27px;
    background: linear-gradient(to bottom, #a9d85c 0%, var(--brand-green) 45%, var(--brand-green-dark) 100%);
    box-shadow: inset 0 1px 0 rgba(255,255,255,0.45), 0 2px 6px rgba(0,0,0,0.5);
    display: flex;
    align-items: center;
    justify-content: center;
    font-family: "Oswald", "Arial Narrow", sans-serif;
    font-weight: 500;
    font-size: 22px;
    color: var(--button-text);
    text-shadow: 0 1px 2px rgba(0,0,0,0.35);
  }
  .cta-arrow {
    position: absolute;
    right: 26px;
    top: 20px;
    width: 14px;
    height: 14px;
  }
  .product-photo {
    position: absolute;
    left: 735px;
    top: 24px;
    width: 428px;
    height: 314px;
    border-radius: 40px;
    background:
      radial-gradient(circle at 250px 110px, #ffffff 0%, rgba(255,255,255,0) 28%),
      linear-gradient(100deg, var(--product-light) 0%, #bfc3c8 38%, #4a4c50 55%, var(--product-dark) 100%);
  }
</style>
</head>
<body>
  <main class="splash-ad">
    <svg class="light-cone" viewBox="0 0 1200 469" aria-hidden="true">
      <defs>
        <linearGradient id="beam" x1="880" y1="130" x2="260" y2="300" gradientUnits="userSpaceOnUse">
          <stop offset="0" stop-color="#ffffff" stop-opacity="0.55"/>
          <stop offset="0.5" stop-color="#ffffff" stop-opacity="0.18"/>
          <stop offset="1" stop-color="#ffffff" stop-opacity="0"/>
        </linearGradient>
      </defs>
      <polygon points="880,90 880,170 250,380 200,220" fill="url(#beam)"/>
    </svg>

    <h1 class="headline">Outdoor<br>Motion Detection<br>Lighting</h1>

    <div class="product-photo" role="img" aria-label="White and black Norvale wireless LED motion sensor spotlights, lit and mounted on swivel brackets"></div>

    <div class="brand">
      <div class="brand-name"><span class="brand-mark"></span>Norvale</div>
      <p class="brand-tagline">Wireless Light Wherever You Need It</p>
    </div>

    <div class="cta-button">Learn More
      <svg class="cta-arrow" viewBox="0 0 14 14" aria-hidden="true">
        <polyline points="4,2 9,7 4,12" fill="none" stroke="#ffffff" stroke-width="2.4" stroke-linecap="round" stroke-linejoin="round"/>
      </svg>
    </div>
  </main>
</body>
</html>
```